Keystone Lending and Capital. We provide MOSTLY residential home mortgages in Florida AND commercial loans for investment properties throughout the United states.
I would love to emulate so of the lender sites that are available on the internet but I would like to have the site as popular as possible for SEO purposes. Clients can already click the link to take them to the mortgage application where they can complete that and upload documents. If you could polish that up for me that would be great. I can also provide you with great detail on loan programs that are currently being offered. WE OFFER ALL MORTGAGE LENDING PRODUCTS. I would also like to add something in reference to the rate but I don't think it's legal to actually state or promise a rate for mortgage since they vary based on loan type, client and other criteria...

On the Keystone real estate site I would like to add a link or some way for clients to be able to put in credit card information to render services ...

Please let me know what you need from me

Thank you !!

Current link to site to improve and code

https://keystonelendingandcapital.example/

Residential and commmercial lending

Requirements
Must have
• Love to integrate Mortgage interest rates even if general
Nice to have
• Link to fill out mortgage application via Vanta LOS software

```html
<!DOCTYPE html>
<html lang="en">
<head>
<meta charset="utf-8">
<title>Keystone Lending and Capital</title>
<link rel="stylesheet" href="https://fonts.googleapis.com/css2?family=Archivo:wght@400;500;600;700;800&family=Inter:wght@400;500;600&display=swap">
<style>
:root{
  --green-dark:#1b2d19;
  --green-deep:#213a1f;
  --lime:#8cc33f;
  --grey-band:#ededed;
  --ink:#1d1d1d;
  --muted:#555;
  --white:#fff;
}
*{box-sizing:border-box;margin:0;padding:0}
html,body{width:1200px;height:4850px;overflow:hidden}
body{position:relative;font-family:"Inter",sans-serif;color:var(--ink);background:var(--white)}
.abs{position:absolute}

/* header */
.hero-photo{left:0;top:0;width:1200px;height:703px;background:linear-gradient(180deg,#a9b6c8 0%,#c9b9a6 25%,#8d5b3c 55%,#3c3b3a 80%,#4a5b2e 100%)}
.topbar{left:437px;top:0;width:763px;height:135px;background:var(--green-dark)}
.contact-row{left:590px;top:50px;display:flex;gap:46px;color:#fff;font-size:12px;align-items:center}
.contact-row span{display:flex;align-items:center;gap:12px}
.social{display:flex;gap:10px}
.social i{display:block;width:26px;height:26px;border-radius:50%;background:#fff}
.main-nav{left:512px;top:97px;display:flex;gap:38px;font-family:"Archivo",sans-serif;font-weight:600;font-size:13px;color:#fff}
.main-nav .active{color:var(--lime)}
.logo-disc{left:110px;top:18px;width:140px;height:140px;border-radius:50%;background:#fff}
.logo-plate{left:180px;top:36px;width:257px;height:99px;background:#fff}
.brand{display:flex;align-items:center;gap:12px}
.brand .mark{width:70px;height:70px;border-radius:50%;background:var(--green-dark)}
.brand .name{font-family:"Archivo",sans-serif;font-weight:800;font-size:9px;color:var(--green-dark);line-height:1.3;width:190px}
.hero-title{left:0;top:195px;width:1200px;text-align:center;font-family:"Archivo",sans-serif;font-weight:800;font-size:36px;line-height:42px;color:var(--green-dark);text-transform:uppercase}
.hero-btn{left:361px;top:341px;width:479px;height:38px;background:var(--green-dark);color:#fff;font-family:"Archivo",sans-serif;font-weight:600;font-size:14px;display:flex;align-items:center;justify-content:center;border-radius:3px}
.hero-arrow{width:28px;height:28px;border:2px solid #fff;border-radius:50%;top:385px}

/* about */
.dots{left:12px;top:790px;width:100px;height:580px;background-image:radial-gradient(#cfcfcf 1.4px,transparent 1.6px);background-size:16px 16px}
.about-main{left:109px;top:790px;width:522px;height:500px;border:5px solid #fff;box-shadow:0 4px 16px rgba(0,0,0,.18);background:linear-gradient(135deg,#8a8580,#4a4a4e 60%,#2e2f33)}
.about-small{left:241px;top:1138px;width:447px;height:275px;border:5px solid #fff;background:linear-gradient(135deg,#c3c8cf,#7f8691)}
.about-copy{left:686px;top:818px;width:420px}
.kicker{font-family:"Archivo",sans-serif;font-weight:700;font-size:31px;color:var(--lime);text-transform:uppercase;line-height:38px}
.h2-dark{font-family:"Archivo",sans-serif;font-weight:700;font-size:31px;color:var(--ink);text-transform:uppercase;line-height:38px}
.about-copy p{margin-top:30px;font-size:11.5px;line-height:26.5px;color:#333}
.stat{display:flex;align-items:center;gap:22px;padding-left:36px;color:#fff}
.stat-green{left:703px;top:1142px;width:216px;height:127px;background:var(--lime)}
.stat-dark{left:703px;top:1287px;width:420px;height:127px;background:var(--green-dark)}
.stat .num{font-family:"Archivo",sans-serif;font-weight:700;font-size:44px;line-height:44px}
.stat .num sup{font-size:20px;vertical-align:top;margin-left:8px}
.stat .lbl{font-family:"Archivo",sans-serif;font-size:14px;letter-spacing:.5px}

/* loan program */
.band-grey{left:0;top:1507px;width:1200px;height:575px;background:var(--grey-band)}
.program-copy{left:110px;top:1645px;width:440px}
.program-copy .lead{margin-top:16px;font-weight:500;font-size:15.5px;line-height:27px}
.program-copy .body{margin-top:14px;font-size:12.5px;line-height:24px;color:var(--muted)}
.btn-dark{display:inline-flex;align-items:center;justify-content:center;background:var(--green-dark);color:#fff;font-family:"Archivo",sans-serif;font-weight:600;font-size:13.5px;height:42px;padding:0 30px;border-radius:2px}
.framed-outline{border:2px solid var(--green-dark);border-radius:18px}
.program-outline{left:621px;top:1616px;width:488px;height:386px}
.program-video{left:601px;top:1598px;width:488px;height:386px;border-radius:18px;background:linear-gradient(135deg,#7c7f70,#4a4d42 60%,#3a3c33)}
.play{left:845px;top:1798px;width:38px;height:38px;border-radius:50%;background:#fff}

/* properties */
.props{left:111px;top:2097px;width:978px;height:669px;border-radius:14px;background:linear-gradient(180deg,#92c13f,#77ad2e)}
.props-title{left:111px;top:2157px;width:978px;text-align:center;font-family:"Archivo",sans-serif;font-weight:600;font-size:30px;color:#fff}
.card{top:2229px;width:283px;height:390px}
.card-label{position:absolute;left:50%;bottom:-12px;transform:translateX(-50%);background:#fff;padding:9px 26px;font-family:"Archivo",sans-serif;font-weight:600;font-size:16px;white-space:nowrap}
.card-label.on{background:var(--green-dark);color:#fff;box-shadow:0 6px 0 #fff}
.pager{top:2676px;width:24px;height:24px;border-radius:50%;border:1.5px solid #fff}

/* products */
.products-title{left:0;top:2850px;width:1200px;text-align:center;font-family:"Archivo",sans-serif;font-weight:700;font-size:31px}
.products-title .accent{color:var(--lime)}
.center-lead{left:190px;width:820px;text-align:center;font-size:15.5px;line-height:27px}
.tab{top:2984px;height:42px;width:240px;display:flex;align-items:center;justify-content:center;font-family:"Archivo",sans-serif;font-weight:600;font-size:14.5px;color:#fff}
.product-list{left:110px;top:3143px;list-style:none}
.product-list li{display:flex;align-items:center;gap:18px;height:44.6px;font-family:"Archivo",sans-serif;font-weight:600;font-size:18px}
.tick{width:26px;height:26px;flex:none}
.products-outline{left:621px;top:3089px;width:488px;height:384px}
.products-photo{left:601px;top:3071px;width:488px;height:384px;border-radius:18px;background:linear-gradient(135deg,#c9bca8,#7e8ea3 55%,#3e4a5c)}

/* insights */
.insights{left:0;top:3565px;width:1200px;height:542px;background:linear-gradient(180deg,var(--green-deep),#1f3a1e)}
.lower-wash{left:0;top:4107px;width:1200px;height:693px;background:#f6f6f5}
.insights-title{left:0;top:3638px;width:1200px;text-align:center;font-family:"Archivo",sans-serif;font-weight:700;font-size:31px;color:#fff}
.rate{display:flex;align-items:center;gap:20px;color:#fff;font-size:16px;white-space:nowrap}
.rate b{font-weight:600}
.chart{left:111px;top:3902px;width:978px;height:399px;border-radius:16px;overflow:hidden;background:linear-gradient(180deg,#0d1d3f 0%,#14295a 55%,#2a2f4a 100%)}

/* footer */
.footer-brand{left:408px;top:4390px}
.footer-brand .mark{width:110px;height:110px}
.footer-brand .name{font-size:10px;width:260px}
.foot-col{top:4572px;width:300px;text-align:center;font-size:13.5px;line-height:20px}
.foot-col .ico{width:34px;height:34px;border-radius:50%;background:var(--green-dark);margin:0 auto 10px;display:flex;align-items:center;justify-content:center}
.foot-col h4{font-family:"Archivo",sans-serif;font-weight:600;font-size:14.5px;margin-bottom:4px}
.foot-social{left:548px;top:4704px;display:flex;gap:8px}
.foot-social i{display:block;width:30px;height:30px;border-radius:50%;background:var(--green-dark)}
.foot-nav{left:0;top:4756px;width:1200px;display:flex;justify-content:center;gap:22px;font-family:"Archivo",sans-serif;font-size:14px}
.bottom-bar{left:0;top:4800px;width:1200px;height:50px;background:var(--green-dark);color:#fff;font-size:13px;display:flex;align-items:center;justify-content:space-between;padding:0 110px}
.bottom-bar nav{display:flex;gap:16px}
</style>
</head>
<body>

<!-- Header & hero -->
<div class="abs hero-photo" role="img" aria-label="Modern apartment buildings with brick and orange facades under a bright sky"></div>
<div class="abs topbar"></div>
<div class="abs contact-row">
  <span><svg width="14" height="14" viewBox="0 0 24 24"><path fill="#8cc33f" d="M6.6 10.8a15 15 0 0 0 6.6 6.6l2.2-2.2a1 1 0 0 1 1-.25 11.4 11.4 0 0 0 3.6.57 1 1 0 0 1 1 1V20a1 1 0 0 1-1 1A17 17 0 0 1 3 4a1 1 0 0 1 1-1h3.5a1 1 0 0 1 1 1c0 1.25.2 2.45.57 3.57a1 1 0 0 1-.25 1z"/></svg>+1 555 010 2040</span>
  <span><svg width="14" height="12" viewBox="0 0 24 20"><rect width="24" height="20" rx="2" fill="#8cc33f"/><path d="M2 3l10 8 10-8" stroke="#1b2d19" stroke-width="2" fill="none"/></svg>info@keystonelending.example</span>
  <span class="social"><i></i><i></i><i></i></span>
</div>
<nav class="abs main-nav">
  <span class="active">HOME</span><span>ABOUT US</span><span>OUR LOAN PROGRAM</span><span>PROPERTIES</span><span>CONTACT US</span>
</nav>
<div class="abs logo-plate"></div>
<div class="abs logo-disc"></div>
<div class="abs brand" style="left:145px;top:52px">
  <div class="mark"></div>
  <div class="name">KEYSTONE LENDING AND CAPITAL OF FLORIDA</div>
</div>
<h1 class="abs hero-title">Your best resource for hassle-free,<br>low cost mortgage<br>origination</h1>
<div class="abs hero-btn">FILL OUT MORTGAGE APPLICATION TO BEGIN LENDING PR</div>
<svg class="abs hero-arrow" style="left:96px" viewBox="0 0 28 28"><path d="M16 8l-6 6 6 6M10 14h10" stroke="#fff" stroke-width="2" fill="none"/></svg>
<svg class="abs hero-arrow" style="left:1076px" viewBox="0 0 28 28"><path d="M12 8l6 6-6 6M18 14H8" stroke="#fff" stroke-width="2" fill="none"/></svg>

<!-- About -->
<div class="abs dots"></div>
<div class="abs about-main" role="img" aria-label="Mortgage advisers shaking hands with a client across an office table"></div>
<div class="abs about-small" role="img" aria-label="Model house on a desk beside financial charts and a laptop"></div>
<div class="abs about-copy">
  <div class="kicker">About Keystone</div>
  <div class="h2-dark">Lending and Capital</div>
  <p>Keystone Lending and Capital Originates Residential Home loans in Florida and Commercial and business financing in all 50 States. We have over 25 years of experience in ALL types of real estate and commercial lending. We are strategically partnered to help you obtain ALL necessary components of residential and commercial lending. From the RIGHT lending partners to the best practice Insurance avenues and commercial and residential real estate partners.</p>
</div>
<div class="abs stat-green stat">
  <svg width="46" height="46" viewBox="0 0 46 46"><circle cx="23" cy="18" r="11" fill="none" stroke="#fff" stroke-width="2.5"/><path d="M23 29v8M10 40h26" stroke="#fff" stroke-width="2.5"/><circle cx="23" cy="18" r="4" fill="#fff"/></svg>
  <div><div class="num">50<sup>+</sup></div><div class="lbl">STATES</div></div>
</div>
<div class="abs stat-dark stat">
  <svg width="46" height="46" viewBox="0 0 46 46"><circle cx="18" cy="13" r="8" fill="#fff"/><path d="M3 40c0-10 7-15 15-15s9 2 11 4" fill="#fff"/><circle cx="33" cy="33" r="9" fill="none" stroke="#fff" stroke-width="2.5"/><path d="M29 33l3 3 5-6" stroke="#fff" stroke-width="2.5" fill="none"/></svg>
  <div><div class="num">25<sup>+</sup></div><div class="lbl">EXPERIENCE</div></div>
</div>

<!-- Loan program -->
<div class="abs band-grey"></div>
<div class="abs program-copy">
  <div class="h2-dark"><span style="color:var(--lime)">OUR LOAN</span> PROGRAM</div>
  <p class="lead">Lorem ipsum dolor sit amet, consectetur adipiscing elit, sed do eiusmod tempor incididunt ut labore.</p>
  <p class="body">Lorem ipsum dolor sit amet, consectetur adipiscing elit, sed do eiusmod tempor incididunt ut labore et dolore magna aliqua. Ut enim ad minim veniam, quis nostrud exercitation ullamco laboris nisi ut aliquip ex ea commodo consequat.Duis aute irure dolor in reprehenderit in voluptate.</p>
  <div class="btn-dark" style="margin-top:26px">LEARN MORE</div>
</div>
<div class="abs framed-outline program-outline"></div>
<div class="abs program-video" role="img" aria-label="Video still of a couple reviewing loan options on a laptop"></div>
<svg class="abs play" viewBox="0 0 38 38"><circle cx="19" cy="19" r="19" fill="#fff"/><path d="M15 12l11 7-11 7z" fill="#1d1d1d"/></svg>

<!-- Properties -->
<div class="abs props"></div>
<div class="abs props-title">AVAILABLE PROPERTIES</div>
<div class="abs card" style="left:155px;background:linear-gradient(160deg,#c8ccd2,#eef0f2 40%,#6c5a48)" role="img" aria-label="White modern townhouse with large windows"><span class="card-label">12 Harbor Lane</span></div>
<div class="abs card" style="left:460px;background:linear-gradient(160deg,#5c6b74,#1e2226 50%,#9a6a3e)" role="img" aria-label="Dark modern house with wooden entrance at dusk"><span class="card-label on">34 Cedar Court</span></div>
<div class="abs card" style="left:765px;background:linear-gradient(160deg,#8c4a32,#5d6670 55%,#a8b4bf)" role="img" aria-label="Modern building with red cladding and grey panels"><span class="card-label">78 Maple Drive</span></div>
<svg class="abs pager" style="left:569px" viewBox="0 0 24 24"><path d="M13 7l-5 5 5 5M8 12h9" stroke="#fff" stroke-width="1.5" fill="none"/></svg>
<svg class="abs pager" style="left:607px;background:#fff" viewBox="0 0 24 24"><path d="M11 7l5 5-5 5M16 12H7" stroke="#1b2d19" stroke-width="1.5" fill="none"/></svg>

<!-- Mortgage lending products -->
<div class="abs products-title"><span class="accent">MORTGAGE</span>&nbsp; LENDING PRODUCTS</div>
<p class="abs center-lead" style="top:2904px">Lorem ipsum dolor sit amet, consectetur adipiscing elit, sed do eiusmod tempor incididunt ut labore et dolore magna aliqua. Ut enim ad minim veniam,</p>
<div class="abs tab" style="left:352px;background:var(--green-dark)">RESIDENTIAL</div>
<div class="abs tab" style="left:609px;background:var(--lime)">COMMERCIAL</div>
<ul class="abs product-list">
  <li><svg class="tick" viewBox="0 0 26 26"><circle cx="13" cy="13" r="13" fill="#1b2d19"/><path d="M7 13l4 4 8-8" stroke="#fff" stroke-width="2.6" fill="none"/></svg>Conventional Loans</li>
  <li><svg class="tick" viewBox="0 0 26 26"><circle cx="13" cy="13" r="13" fill="#1b2d19"/><path d="M7 13l4 4 8-8" stroke="#fff" stroke-width="2.6" fill="none"/></svg>FHA Loans</li>
  <li><svg class="tick" viewBox="0 0 26 26"><circle cx="13" cy="13" r="13" fill="#1b2d19"/><path d="M7 13l4 4 8-8" stroke="#fff" stroke-width="2.6" fill="none"/></svg>VA Loans</li>
  <li><svg class="tick" viewBox="0 0 26 26"><circle cx="13" cy="13" r="13" fill="#1b2d19"/><path d="M7 13l4 4 8-8" stroke="#fff" stroke-width="2.6" fill="none"/></svg>USDA Loans</li>
  <li><svg class="tick" viewBox="0 0 26 26"><circle cx="13" cy="13" r="13" fill="#1b2d19"/><path d="M7 13l4 4 8-8" stroke="#fff" stroke-width="2.6" fill="none"/></svg>Jumbo Loans</li>
  <li><svg class="tick" viewBox="0 0 26 26"><circle cx="13" cy="13" r="13" fill="#1b2d19"/><path d="M7 13l4 4 8-8" stroke="#fff" stroke-width="2.6" fill="none"/></svg>Adjustable-Rate Mortgages (ARMs)</li>
</ul>
<div class="abs framed-outline products-outline"></div>
<div class="abs products-photo" role="img" aria-label="Smiling couple shaking hands with a loan officer"></div>

<!-- Market insights -->
<div class="abs insights"></div>
<div class="abs lower-wash"></div>
<div class="abs insights-title">CURRENT MORTGAGE MARKET INSIGHTS</div>
<p class="abs center-lead" style="top:3695px;color:#fff">Lorem ipsum dolor sit amet, consectetur adipiscing elit, sed do eiusmod tempor incididunt ut labore et dolore magna aliqua. Ut enim ad minim veniam,</p>
<div class="abs rate" style="left:432px;top:3780px"><svg class="tick" viewBox="0 0 26 26"><circle cx="13" cy="13" r="13" fill="#fff"/><path d="M7 13l4 4 8-8" stroke="#1b2d19" stroke-width="2.6" fill="none"/></svg><span>15-year fixed-rate mortgage: <b>5.875%</b></span></div>
<div class="abs rate" style="left:110px;top:3831px"><svg class="tick" viewBox="0 0 26 26"><circle cx="13" cy="13" r="13" fill="#fff"/><path d="M7 13l4 4 8-8" stroke="#1b2d19" stroke-width="2.6" fill="none"/></svg><span>30-year fixed-rate mortgage: <b>7.124%</b></span></div>
<div class="abs rate" style="left:665px;top:3831px"><svg class="tick" viewBox="0 0 26 26"><circle cx="13" cy="13" r="13" fill="#fff"/><path d="M7 13l4 4 8-8" stroke="#1b2d19" stroke-width="2.6" fill="none"/></svg><span>5-year adjustable-rate mortgage (ARM): <b>7.336%</b></span></div>
<div class="abs chart" role="img" aria-label="Line chart of mortgage rate trends set over a night city skyline photo">
  <svg width="978" height="399" viewBox="0 0 978 399">
    <g stroke="#33466f" stroke-width="1"><path d="M100 30h820M100 80h820M100 130h820M100 180h820M100 230h820M100 280h820M100 330h820"/></g>
    <polyline points="115,360 170,320 230,290 300,250 350,200 420,150 480,190 540,110 600,160 640,70 720,140 780,90 870,40" fill="none" stroke="#e8eef8" stroke-width="2"/>
    <polyline points="115,380 180,350 260,310 330,280 390,240 460,210 520,230 590,180 650,160 720,120 780,80 840,105" fill="none" stroke="#d0202e" stroke-width="2" stroke-dasharray="5 4"/>
    <g fill="#d0202e"><circle cx="460" cy="210" r="4"/><circle cx="590" cy="180" r="4"/><circle cx="780" cy="80" r="4"/><circle cx="840" cy="105" r="4"/><circle cx="330" cy="280" r="4"/></g>
  </svg>
</div>

<!-- Footer -->
<div class="abs brand footer-brand"><div class="mark"></div><div class="name">KEYSTONE LENDING AND CAPITAL OF FLORIDA</div></div>
<div class="abs foot-col" style="left:206px">
  <div class="ico"><svg width="16" height="16" viewBox="0 0 24 24"><path fill="#fff" d="M6.6 10.8a15 15 0 0 0 6.6 6.6l2.2-2.2a1 1 0 0 1 1-.25 11.4 11.4 0 0 0 3.6.57 1 1 0 0 1 1 1V20a1 1 0 0 1-1 1A17 17 0 0 1 3 4a1 1 0 0 1 1-1h3.5a1 1 0 0 1 1 1c0 1.25.2 2.450.57 3.57a1 1 0 0 1-.25 1z"/></svg></div>
  <h4>PHONE</h4><p>+1 555 010 2040</p>
</div>
<div class="abs foot-col" style="left:425px">
  <div class="ico"><svg width="14" height="18" viewBox="0 0 14 18"><path d="M7 0a7 7 0 0 1 7 7c0 5-7 11-7 11S0 12 0 7a7 7 0 0 1 7-7z" fill="#fff"/><circle cx="7" cy="7" r="2.5" fill="#1b2d19"/></svg></div>
  <h4>LOCATION</h4><p>United States,<br>Keystone Lending and Capital</p>
</div>
<div class="abs foot-col" style="left:669px">
  <div class="ico"><svg width="16" height="12" viewBox="0 0 24 18"><rect width="24" height="18" rx="2" fill="#fff"/><path d="M2 3l10 7 10-7" stroke="#1b2d19" stroke-width="2" fill="none"/></svg></div>
  <h4>EMAIL</h4><p>info@keystonelending.example</p>
</div>
<div class="abs foot-social"><i></i><i></i><i></i></div>
<nav class="abs foot-nav"><span>HOME</span><span>|</span><span>ABOUT US</span><span>|</span><span>OUR LOAN PROGRAM</span><span>|</span><span>PROPERTIES</span><span>|</span><span>CONTACT US</span></nav>
<footer class="abs bottom-bar">
  <span>© 2025 Keystone Lending and Capital. All rights reserved.</span>
  <nav><span>Privacy</span><span>|</span><span>Terms of Use</span></nav>
</footer>

</body>
</html>
```